Employee Benefits and Insurance Consulting

We are an existing company with over 30 years experience but are changing our name. We would like a simple design with grey tones.

Industry/Entity Type

Insurance

Contact Information for Business Card

Marlow Benefits Consulting
Gerald P Odell CEO
5172 Brackenfield Road
Ashford Falls, TN 37946
gerald@marlowbx.com
865-412-3396 - O
865-247-5081 - C

```html
<!DOCTYPE html>
<html lang="en">
<head>
<meta charset="utf-8">
<title>Marlow Benefits Consulting – Business Card</title>
<link rel="stylesheet" href="https://fonts.googleapis.com/css2?family=Arimo:wght@400;700&family=Libre+Baskerville:ital@1&display=swap">
<style>
  :root {
    --page: #ffffff;
    --ink: #0d0d0d;
    --brand-slate: #3e4d57;
    --teal-light: #b9d8d3;
    --teal-mid: #8cc1b9;
    --teal-deep: #5d9e94;
    --band-dark: #1c564d;
    --band-bright: #32b3a0;
    --email: #ffffff;
  }
  * { margin: 0; padding: 0; box-sizing: border-box; }
  html, body {
    width: 1200px;
    height: 702px;
    overflow: hidden;
    background: var(--page);
  }
  .card {
    position: absolute;
    left: 44px;
    top: 44px;
    width: 1115px;
    height: 615px;
    overflow: hidden;
    font-family: "Arimo", Arial, sans-serif;
    color: var(--ink);
    box-shadow: 0 0 3px rgba(0,0,0,0.12);
  }
  .card__art {
    position: absolute;
    inset: 0;
    width: 100%;
    height: 100%;
  }
  .brand {
    position: absolute;
    left: 62px;
    top: 62px;
    display: flex;
    align-items: center;
    gap: 22px;
    color: var(--brand-slate);
  }
  .brand__dot {
    width: 74px;
    height: 74px;
    border-radius: 50%;
    background: var(--brand-slate);
  }
  .brand__name {
    font-weight: 400;
    line-height: 1;
  }
  .brand__name-main {
    display: block;
    font-size: 104px;
    letter-spacing: -1px;
  }
  .brand__name-sub {
    display: block;
    font-size: 29px;
    font-variant: small-caps;
    letter-spacing: 1px;
    margin-top: 10px;
    margin-left: 40px;
  }
  .contact {
    position: absolute;
    left: 773px;
    top: 160px;
  }
  .contact__name {
    font-size: 37px;
    font-weight: 400;
    letter-spacing: 0.2px;
    text-shadow: 0 0 4px rgba(255,255,255,0.9), 1px 1px 2px rgba(0,0,0,0.25);
  }
  .contact__role {
    font-family: "Libre Baskerville", Georgia, serif;
    font-style: italic;
    font-size: 20px;
    margin-left: 122px;
    margin-top: 2px;
  }
  .contact__phones {
    list-style: none;
    margin-top: 100px;
    margin-left: 8px;
  }
  .contact__phone {
    display: flex;
    align-items: center;
    gap: 16px;
    font-size: 22px;
    height: 32px;
  }
  .contact__phone svg { width: 26px; height: 26px; }
  .contact__address {
    font-style: normal;
    font-size: 20px;
    line-height: 30px;
    margin-top: 42px;
    margin-left: 7px;
  }
  .contact__email {
    position: absolute;
    left: 0;
    width: 1115px;
    top: 553px;
    padding-left: 82px;
    text-align: center;
    font-size: 31px;
    color: var(--email);
    letter-spacing: 0.3px;
  }
</style>
</head>
<body>
<main class="card">
  <svg class="card__art" viewBox="0 0 1003 553" preserveAspectRatio="none" aria-hidden="true">
    <defs>
      <linearGradient id="field" x1="0" y1="0" x2="1" y2="1">
        <stop offset="0" stop-color="#c9e3df"/>
        <stop offset="0.55" stop-color="#afd3cd"/>
        <stop offset="1" stop-color="#8fc2ba"/>
      </linearGradient>
      <linearGradient id="fold" x1="0" y1="0" x2="1" y2="0">
        <stop offset="0" stop-color="#9ccbc3"/>
        <stop offset="0.4" stop-color="#79b2a8"/>
        <stop offset="1" stop-color="#5d9e94"/>
      </linearGradient>
      <linearGradient id="band" x1="1" y1="0" x2="0" y2="1">
        <stop offset="0" stop-color="#1c564d"/>
        <stop offset="0.3" stop-color="#32b3a0"/>
        <stop offset="0.7" stop-color="#2ea796"/>
        <stop offset="1" stop-color="#1c564d"/>
      </linearGradient>
    </defs>
    <rect class="art__field" width="1003" height="553" fill="url(#field)"/>
    <path class="art__fold" d="M868 0 C905 140 880 330 950 470 C965 500 985 520 1003 530 V0 Z" fill="url(#fold)"/>
    <path class="art__gap" d="M740 0 H752 C680 235 420 425 0 462 V455 C400 420 668 230 740 0 Z" fill="#ffffff"/>
    <path class="art__band" d="M680 0 H740 C668 230 400 420 0 455 V444 C380 405 610 220 680 0 Z" fill="url(#band)"/>
    <path class="art__white" d="M0 0 H680 C610 220 380 405 0 444 Z" fill="#ffffff"/>
  </svg>

  <div class="brand">
    <span class="brand__dot"></span>
    <h1 class="brand__name">
      <span class="brand__name-main">Marlow</span>
      <span class="brand__name-sub">Benefits Consulting</span>
    </h1>
  </div>

  <section class="contact">
    <h2 class="contact__name">Gerald P Odell</h2>
    <p class="contact__role">(CEO)</p>
    <ul class="contact__phones">
      <li class="contact__phone">
        <svg viewBox="0 0 26 26" aria-label="Mobile">
          <circle cx="13" cy="13" r="12" fill="none" stroke="#111" stroke-width="1.6"/>
          <rect x="9" y="5" width="8" height="16" rx="1.5" fill="none" stroke="#111" stroke-width="1.5"/>
          <rect x="10.5" y="7" width="5" height="4" fill="#111"/>
          <path d="M10.5 13h5M10.5 15.5h5M10.5 18h5" stroke="#111" stroke-width="1"/>
        </svg>
        <span>865-247-5081</span>
      </li>
      <li class="contact__phone">
        <svg viewBox="0 0 26 26" aria-label="Office">
          <circle cx="13" cy="13" r="12.5" fill="#111"/>
          <path d="M8.5 6.5c1-.6 1.8-.3 2.3.6l1.2 2.3c.4.8.2 1.5-.5 2l-.9.6c.6 1.6 1.8 3 3.4 3.9l.7-.8c.6-.6 1.3-.7 2-.3l2.2 1.4c.8.5 1 1.3.4 2.2-.9 1.4-2.3 2-3.9 1.5-4.2-1.3-7.5-4.9-8.4-9.2-.3-1.6.3-3.3 1.5-4.2z" fill="#fff"/>
        </svg>
        <span>865-412-3396</span>
      </li>
    </ul>
    <address class="contact__address">
      5172 Brackenfield Road<br>
      Ashford Falls, TN 37946
    </address>
  </section>

  <p class="contact__email">gerald@marlowbx.com</p>
</main>
</body>
</html>
```